Designing of Orientation Materials and Innovative Ways to ‘Market’ Procurement Function

To Market and promote Procurement function and it’s ‘real’ capabilities clearly, to demonstrate that the function is an enabler instead being perceive as a barrier to other internal functions. Sometimes due to the lack of a common language even makes it difficult for other functions (e.g) Marketing and Procurement to understand each other’s aims and intentions.
The audience could be from all functions such as; Human Resource, Finance, Sales & Marketing, Supply Chain/Procurement, Corporate Affairs and Information System.

```html
<!DOCTYPE html>
<html lang="en">
<head>
<meta charset="utf-8">
<title>Procurement's Evolving Value Proposition</title>
<link href="https://fonts.googleapis.com/css2?family=Source+Sans+3:wght@400;600;700&display=swap" rel="stylesheet">
<style>
  :root {
    --page-bg: #e9e9e9;
    --poster-bg: #f4f4f4;
    --brand-blue: #3a8fd0;
    --label-blue: #2e86c6;
    --text-green: #2a9f4c;
    --panel-grey: #e3e3e5;
    --tier-orange: #f29a45;
    --tier-green: #7dc862;
    --tier-teal: #3cbfc8;
    --tier-blue: #3592cc;
    --white: #ffffff;
  }
  * { box-sizing: border-box; margin: 0; padding: 0; }
  html, body { width: 1200px; height: 882px; overflow: hidden; }
  body {
    background: var(--page-bg);
    font-family: "Source Sans 3", "Source Sans Pro", Arial, sans-serif;
    position: relative;
  }
  .poster {
    position: absolute;
    left: 0; top: 62px;
    width: 1200px; height: 758px;
    background: var(--poster-bg);
  }
  .poster-header {
    position: absolute; left: 0; top: 0;
    width: 100%; height: 100px;
    background: var(--brand-blue);
    display: flex; align-items: center; justify-content: center;
  }
  .poster-title {
    color: var(--white);
    font-weight: 700;
    font-size: 40px;
    letter-spacing: 0.5px;
  }
  .poster-footer {
    position: absolute; left: 0; bottom: 0;
    width: 100%; height: 22px;
    background: var(--brand-blue);
  }
  .axis-label {
    position: absolute;
    width: 200px;
    text-align: center;
    color: var(--label-blue);
    font-weight: 700;
    font-size: 17px;
    letter-spacing: 0.3px;
  }
  .axis-arrow { position: absolute; }
  .tier {
    position: absolute;
    left: 221px;
    width: 946px;
    height: 113px;
  }
  .tier-shape { position: absolute; left: 0; top: 0; }
  .tier-name {
    position: absolute;
    left: 34px; top: 0;
    width: 515px; height: 113px;
    display: flex; align-items: center; justify-content: center;
    text-align: center;
    color: var(--white);
    font-weight: 700;
    font-size: 25px;
    line-height: 25px;
    letter-spacing: 0.4px;
  }
  .tier-note {
    position: absolute;
    left: 598px; top: 0;
    width: 340px; height: 113px;
    display: flex; align-items: center;
    font-size: 20.5px;
    line-height: 26px;
  }
  .tier-note strong { font-weight: 700; }
  .note-blue { color: var(--label-blue); }
  .note-green { color: var(--text-green); }
</style>
</head>
<body>
  <main class="poster">
    <header class="poster-header">
      <h1 class="poster-title">PROCUREMENT’S EVOLVING VALUE PROPOSITION</h1>
    </header>

    <div class="axis-label" style="left:22px; top:146px;">SUPPLIER CENTRIC</div>
    <svg class="axis-arrow" style="left:98px; top:180px;" width="44" height="204" viewBox="0 0 44 204" aria-hidden="true">
      <defs>
        <linearGradient id="margin-gradient" x1="0" y1="1" x2="0" y2="0">
          <stop offset="0" stop-color="#7dc862"/>
          <stop offset="0.5" stop-color="#f2cf4a"/>
          <stop offset="1" stop-color="#f29a45"/>
        </linearGradient>
      </defs>
      <path d="M8 24 L22 2 L36 24 L35.5 24 L35.5 190 Q35.5 202 22 202 Q8.5 202 8.5 190 L8.5 24 Z" fill="url(#margin-gradient)"/>
      <path d="M3 27 L22 4 L41 27 Z" fill="#f29a45"/>
      <text x="0" y="0" transform="translate(28 180) rotate(-90)" font-family="Source Sans 3, sans-serif" font-size="15" fill="#e58a3a">Enhance Margins</text>
    </svg>

    <div class="axis-label" style="left:18px; top:398px;">VALUE INFLECTION</div>
    <svg class="axis-arrow" style="left:96px; top:440px;" width="44" height="194" viewBox="0 0 44 194" aria-hidden="true">
      <defs>
        <linearGradient id="savings-gradient" x1="0" y1="1" x2="0" y2="0">
          <stop offset="0" stop-color="#3592cc"/>
          <stop offset="1" stop-color="#3cbf9c"/>
        </linearGradient>
      </defs>
      <path d="M8.5 24 L35.5 24 L35.5 180 Q35.5 192 22 192 Q8.5 192 8.5 180 Z" fill="url(#savings-gradient)"/>
      <path d="M3 27 L22 4 L41 27 Z" fill="#3cbf9c"/>
      <text x="0" y="0" transform="translate(28 168) rotate(-90)" font-family="Source Sans 3, sans-serif" font-size="15" fill="#2e7fc0">Deliver Savings</text>
    </svg>

    <div class="axis-label" style="left:12px; top:648px;">CATEGORY CENTRIC</div>

    <section class="tier" style="top:173px;">
      <svg class="tier-shape" width="946" height="113" viewBox="0 0 946 113" aria-hidden="true">
        <rect x="540" y="0" width="406" height="113" fill="var(--panel-grey)"/>
        <polygon points="34,0 549,0 583,56.5 549,113 34,113 0,56.5" fill="var(--tier-orange)"/>
      </svg>
      <div class="tier-name">TOTAL ENTERPRICE</div>
      <p class="tier-note note-blue"><span><strong>Global interests</strong> sought to capture cross business benefits above individual interests</span></p>
    </section>

    <section class="tier" style="top:293px;">
      <svg class="tier-shape" width="946" height="113" viewBox="0 0 946 113" aria-hidden="true">
        <rect x="540" y="0" width="406" height="113" fill="var(--panel-grey)"/>
        <polygon points="34,0 549,0 583,56.5 549,113 34,113 0,56.5" fill="var(--tier-green)"/>
      </svg>
      <div class="tier-name">STRATEGIC SOURCING AND CATEGORY<br>MANAGEMENT</div>
      <p class="tier-note note-blue"><span><strong>Competitive advantage</strong> through supplier collaboration to drive innovation annd growth</span></p>
    </section>

    <section class="tier" style="top:415px;">
      <svg class="tier-shape" width="946" height="113" viewBox="0 0 946 113" aria-hidden="true">
        <rect x="540" y="0" width="406" height="113" fill="var(--panel-grey)"/>
        <polygon points="34,0 549,0 583,56.5 549,113 34,113 0,56.5" fill="var(--tier-teal)"/>
      </svg>
      <div class="tier-name">AP TRANSACTIONAL EFFICIENCIES</div>
      <p class="tier-note note-green"><span><strong>Improve total cost of ownership</strong> through optimisation of purchasing</span></p>
    </section>

    <section class="tier" style="top:535px;">
      <svg class="tier-shape" width="946" height="113" viewBox="0 0 946 113" aria-hidden="true">
        <rect x="540" y="0" width="406" height="113" fill="var(--panel-grey)"/>
        <polygon points="34,0 549,0 583,56.5 549,113 34,113 0,56.5" fill="var(--tier-blue)"/>
      </svg>
      <div class="tier-name">SUPPLIER RELATIONSHIP<br>MANAGEMENT</div>
      <p class="tier-note note-green"><span><strong>Cost out</strong> through process efficiency</span></p>
    </section>

    <div class="poster-footer"></div>
  </main>
</body>
</html>
```